Website for an electrical contractor :)

We are after a web site which can show pictures of our jobs and our capability in a professional, creative and easily understood way.

----- Bramwell Electrical ------

We really want a visually good looking website with three sections

Section one:
'Completed projects'
We have a few pictures of jobs which we've completed and would like to show off with a brief description. (see uploads)

Section two:
'Our capabilities'
Just a list of what services we offer

Section three:
We would like a 'contact us' section which people can send us a short msg and upload a file for plans to be able to send to us. We would need their name, phone number and email details. We would also need a short privacy policy saying 'we do not disclose information to third parties'.
We also want to display our contact number and postal address

Good luck :)

Target Market(s)

Adults 25 years+
Business owners
Builders
Real estate agents

Industry/Entity Type

Electrical

Colors

Designer to choose colors to be used in the design.

Requirements
Must have
• Visually appealing
Easy to understand
In the 'Completed projects' section, must have a list for each project we do i can upload pictures for it.

```html
<!DOCTYPE html>
<html lang="en">
<head>
<meta charset="utf-8">
<title>Bramwell Electrical &amp; Communications</title>
<link href="https://fonts.googleapis.com/css2?family=Bebas+Neue&family=Arimo:wght@400;700&display=swap" rel="stylesheet">
<style>
:root{
  --red:#e0262a;
  --red-deep:#c81f23;
  --charcoal:#333333;
  --grey-text:#555555;
  --light-grey:#888888;
  --white:#ffffff;
  --button-dark:#4a4a4a;
}
*{box-sizing:border-box;margin:0;padding:0}
html,body{width:1200px;height:1000px;overflow:hidden;background:var(--white);font-family:"Arimo",Arial,sans-serif;color:var(--grey-text)}
.page{position:relative;width:1200px;height:1000px}
.site-header{position:absolute;left:307px;top:0;width:596px;height:87px}
.brand{position:absolute;left:0;top:22px;display:flex;align-items:center;gap:10px}
.brand-dot{width:36px;height:36px;border-radius:50%;background:var(--red)}
.brand-name{font-size:36px;font-weight:400;color:var(--grey-text);letter-spacing:-0.5px;line-height:44px}
.header-contact{position:absolute;right:0;top:34px;text-align:right;font-size:12px;line-height:15px;color:var(--grey-text)}
.header-contact strong{font-weight:700}
.main-nav{position:absolute;left:143px;top:87px;width:915px;height:26px;background:var(--charcoal)}
.main-nav a{position:absolute;top:7px;color:var(--white);font-size:10px;line-height:12px;text-decoration:none;white-space:nowrap}
.main-nav a.current{color:var(--light-grey)}
.nav-home{left:164px}
.nav-capabilities{left:306px}
.nav-projects{left:482px}
.nav-contact{right:156px}
.hero{position:absolute;left:143px;top:113px;width:915px;height:324px;background:linear-gradient(100deg,#e8432a 0%,#d33a24 28%,#8a8a88 45%,#f1f1f3 60%,#ffffff 100%)}
.welcome{position:absolute;left:143px;top:437px;width:915px;height:138px;text-align:center;background:linear-gradient(#eeeeee,#ffffff 14px)}
.welcome h1{font-family:"Bebas Neue",sans-serif;font-weight:400;font-size:20px;line-height:24px;color:var(--red);margin-top:22px;letter-spacing:0.2px}
.welcome h1 span{color:var(--grey-text)}
.welcome p{width:480px;margin:4px auto 0;font-size:9.5px;line-height:14px;color:var(--grey-text)}
.btn-small{display:inline-block;height:15px;line-height:15px;padding:0 10px;border-radius:3px;font-size:7px;text-transform:uppercase;text-decoration:none}
.btn-dark{background:var(--button-dark);color:var(--white);margin-top:4px}
.btn-light{background:var(--white);color:var(--charcoal);border:1px solid #ccc}
.services{position:absolute;left:143px;top:575px;width:915px;height:257px;background:linear-gradient(135deg,var(--red) 0%,var(--red-deep) 100%)}
.services h2{font-family:"Bebas Neue",sans-serif;font-weight:400;font-size:19px;color:var(--white);text-align:center;margin-top:21px}
.service-list{position:absolute;left:227px;top:58px;display:flex;gap:7px}
.service-card{width:233px}
.service-photo{width:233px;height:111px;border:1px solid #e6e6e6}
.photo-commercial{background:linear-gradient(#5b8fd8 0%,#9ebfe8 35%,#d9d6cf 60%,#b8a990 100%)}
.photo-residential{background:linear-gradient(#6d9ad8 0%,#c9c29a 40%,#6d6a5e 70%,#8c8470 100%)}
.service-card h3{font-size:10px;font-weight:700;color:var(--white);margin-top:9px;text-transform:uppercase}
.service-card p{font-size:8px;line-height:12px;color:var(--white);margin:3px 0 5px}
.call-band{position:absolute;left:307px;top:865px;width:596px;height:50px;display:flex;align-items:center;justify-content:space-between}
.call-info{display:flex;align-items:center;gap:12px;font-size:20px;color:var(--grey-text)}
.call-info strong{font-weight:700}
.btn-contact{display:block;width:128px;height:33px;line-height:33px;text-align:center;background:var(--button-dark);color:var(--white);border-radius:3px;font-size:15px;text-decoration:none;box-shadow:0 1px 2px rgba(0,0,0,.4)}
.site-footer{position:absolute;left:143px;top:941px;width:915px;height:59px;background:var(--charcoal);color:var(--white)}
.footer-nav{position:absolute;left:164px;top:27px;font-size:6.5px;line-height:9px;white-space:nowrap}
.footer-nav a{color:var(--white);text-decoration:none}
.footer-nav a.current{color:var(--light-grey)}
.footer-nav .sep{margin:0 3px}
.footer-copy{font-size:6px;margin-top:2px}
.social{position:absolute;right:223px;top:30px;text-align:right;font-size:6px;line-height:8px;white-space:nowrap}
.social-icons{position:absolute;right:156px;top:29px;display:flex;gap:14px}
.social-icons span{width:16px;height:16px;border-radius:50%;background:var(--white);display:block}
</style>
</head>
<body>
<div class="page">
  <header class="site-header">
    <div class="brand"><span class="brand-dot"></span><span class="brand-name">Bramwell</span></div>
    <div class="header-contact">Phone: 0400 318 627<br><strong>info@bramwell.com.au</strong></div>
  </header>

  <nav class="main-nav">
    <a class="nav-home current" href="#">HOME</a>
    <a class="nav-capabilities" href="#">CAPABILITIES</a>
    <a class="nav-projects" href="#">COMPLETED PROJECTS</a>
    <a class="nav-contact" href="#">CONTACT US</a>
  </nav>

  <div class="hero" role="img" aria-label="Photo of red-handled pliers resting on rolled electrical wiring plans"></div>

  <section class="welcome">
    <h1>Welcome to <span>Bramwell</span> Electrical &amp; Communications</h1>
    <p>Lorem Ipsum has been the industry's standard dummy text ever since the 1500s, when an unknown printer took a galley of type and scrambled it to make a type specimen book. It has survived not only five centuries, but also the leap into electronic typesetting, remaining essentially unchanged.</p>
    <a class="btn-small btn-dark" href="#">Read more</a>
  </section>

  <section class="services">
    <h2>Services</h2>
    <div class="service-list">
      <div class="service-card">
        <div class="service-photo photo-commercial" role="img" aria-label="Photo of a new commercial warehouse building under blue sky"></div>
        <h3>Commercial / Industrial</h3>
        <p>Nullam blandit vulputate maximus. Integer sit amet turpis sit amet neque venenatis congue et a sem. Maecenas sit tempor.</p>
        <a class="btn-small btn-light" href="#">Read more</a>
      </div>
      <div class="service-card">
        <div class="service-photo photo-residential" role="img" aria-label="Photo of a paved residential driveway between new townhouses"></div>
        <h3>Residential</h3>
        <p>Nullam blandit vulputate maximus. Integer sit amet turpis sit amet neque venenatis congue et a sem. Maecenas sit tempor.</p>
        <a class="btn-small btn-light" href="#">Read more</a>
      </div>
    </div>
  </section>

  <section class="call-band">
    <div class="call-info">
      <svg width="50" height="50" viewBox="0 0 50 50" aria-hidden="true">
        <circle cx="25" cy="25" r="23" fill="none" stroke="#555" stroke-width="2.5"/>
        <path d="M17 15c2-1 3 0 4 2l1 3c0 1-1 2-2 3 1 3 3 5 6 6 1-1 2-2 3-2l3 1c2 1 3 2 2 4-1 2-3 3-5 3-7-1-13-7-14-14 0-3 1-5 2-6z" fill="#555"/>
        <path d="M28 17a6 6 0 0 1 5 5M28 13a10 10 0 0 1 9 9" fill="none" stroke="#555" stroke-width="1.8" stroke-linecap="round"/>
      </svg>
      <span>Call us now on <strong>0400 318 627</strong></span>
    </div>
    <a class="btn-contact" href="#">CONTACT US</a>
  </section>

  <footer class="site-footer">
    <div class="footer-nav">
      <a class="current" href="#">HOME</a><span class="sep">|</span><a href="#">CAPABILITIES</a><span class="sep">|</span><a href="#">COMPLETED PROJECTS</a><span class="sep">|</span><a href="#">CONTACT US</a>
      <div class="footer-copy">© 2015 Privacy Policy</div>
    </div>
    <div class="social">SOCIAL NETWORKS<br>Lorem Ipsum is placeholder text</div>
    <div class="social-icons"><span></span><span></span></div>
  </footer>
</div>
</body>
</html>
```